Park Company Mobile Application Design

We are looking for deisgn of the mobile application for the parking company. More details about the parking company you can find on the following web site: www.tvr.mk.
As well we attached the parking card that this company is issuing. As you may see their preferred color is green.
Attached you can find screens that we are planning to implement in the mobile application.
If you need more details please contact us on goran@brelo.mk.

Thanks,
Goran Dimovski
Brelo Group

```html
<!DOCTYPE html>
<html lang="mk">
<head>
<meta charset="utf-8">
<title>Градски Паркинг – мобилна апликација</title>
<link rel="stylesheet" href="https://fonts.googleapis.com/css2?family=Montserrat:wght@400;500;700;800;900&display=swap">
<style>
  :root{
    --page:#f1f3f4;
    --screen:#2b3744;
    --screen-top:#303d4a;
    --field:#3a4b5c;
    --label:#93a0ad;
    --green:#58b74c;
    --green-bright:#3dcc25;
    --green-glow:rgba(88,183,76,.45);
    --ink-dark:#0f2a0a;
    --white:#ffffff;
  }
  *{box-sizing:border-box;margin:0;padding:0}
  html,body{width:882px;height:1200px;overflow:hidden}
  body{background:var(--page);font-family:"Montserrat",sans-serif;position:relative}

  .brand{position:absolute;left:44px;top:84px;display:flex;align-items:center;gap:12px}
  .brand-dot{width:34px;height:34px;border-radius:50%;background:var(--green)}
  .brand-name{font-size:28px;font-weight:800;color:var(--green);letter-spacing:.5px}

  .screens{position:absolute;left:31px;top:210px;display:flex;gap:20px;align-items:flex-start}
  .screen{width:190px;height:400px;border-radius:26px;background:linear-gradient(180deg,var(--screen-top),var(--screen));
    position:relative;overflow:hidden;padding:26px 16px 0;display:flex;flex-direction:column;gap:10px}
  .screen:nth-child(2){margin-top:40px}
  .screen:nth-child(3){margin-top:80px}
  .screen:nth-child(4){margin-top:120px}

  .screen-brand{display:flex;align-items:center;justify-content:center;gap:6px;margin-bottom:10px}
  .screen-brand .brand-dot{width:14px;height:14px}
  .screen-brand .brand-name{font-size:12px}

  .field{background:var(--field);border-radius:8px;padding:8px 10px;min-height:44px}
  .field-label{font-size:8px;color:var(--label);margin-bottom:5px}
  .field-value{font-size:10px;color:var(--green);font-weight:500;white-space:nowrap;overflow:hidden}
  .field-dots{font-size:13px;letter-spacing:2px;color:var(--green);line-height:1}
  .field.active{box-shadow:0 0 0 1px var(--green),0 0 10px var(--green-glow)}

  .link{font-size:9px;color:var(--green);text-align:center;margin:6px 0}
  .option{display:flex;align-items:center;gap:7px;font-size:8.5px;color:var(--label)}
  .option svg{flex:none}

  .btn{border-radius:8px;height:34px;display:flex;align-items:center;justify-content:center;
    font-size:9px;font-weight:800;letter-spacing:1.5px;text-transform:uppercase}
  .btn-primary{background:var(--green);color:var(--white);box-shadow:0 0 14px var(--green-glow)}
  .btn-secondary{background:var(--field);color:var(--green)}
  .spacer{flex:1}
  .bottom-gap{height:22px}

  .tabbar{margin:0 -16px;height:58px;background:var(--field);display:flex;justify-content:space-around;align-items:center}
  .tab{display:flex;flex-direction:column;align-items:center;gap:4px;font-size:7.5px;font-weight:700;color:var(--white);letter-spacing:.5px}

  .thanks{position:absolute;left:250px;top:970px;width:392px;height:200px}
  .thanks-bubble{position:absolute;inset:0;width:100%;height:100%;filter:drop-shadow(0 10px 16px rgba(61,204,37,.3))}
  .thanks-text{position:absolute;left:0;right:0;top:52px;text-align:center;font-size:50px;font-weight:900;color:var(--ink-dark);letter-spacing:1px}
</style>
</head>
<body>

<header class="brand">
  <span class="brand-dot"></span>
  <span class="brand-name">Градски Паркинг</span>
</header>

<main class="screens">
  <section class="screen screen-login">
    <div class="screen-brand"><span class="brand-dot"></span><span class="brand-name">Градски Паркинг</span></div>
    <div class="field"><div class="field-label">Е Пошта</div><div class="field-value">marko.ilievski@posta.mk</div></div>
    <div class="field"><div class="field-label">Лозинка</div><div class="field-dots">●●●●●●●●●</div></div>
    <div class="link">ЗАБОРАВЕНА ЛОЗИНКА</div>
    <div class="spacer"></div>
    <div class="btn btn-primary">Регистрација</div>
    <div class="btn btn-secondary">Најава</div>
    <div class="bottom-gap"></div>
  </section>

  <section class="screen screen-register">
    <div class="screen-brand"><span class="brand-dot"></span><span class="brand-name">Градски Паркинг</span></div>
    <div class="field"><div class="field-label">Е Пошта</div><div class="field-value">marko.ilievski@posta.mk</div></div>
    <div class="field"><div class="field-label">Лозинка</div><div class="field-dots">●●●●●●●●</div></div>
    <div class="field"><div class="field-label">Потврди ја лозинката</div><div class="field-dots">●●●●●●●●</div></div>
    <div class="field active"><div class="field-label">Мобилен</div><div class="field-value">070 456 7890 |</div></div>
    <div class="spacer"></div>
    <div class="btn btn-primary">Регистрирај се</div>
    <div class="bottom-gap"></div>
  </section>

  <section class="screen screen-reset">
    <div class="screen-brand"><span class="brand-dot"></span><span class="brand-name">Градски Паркинг</span></div>
    <div class="field"><div class="field-label">Е Пошта</div><div class="field-value">marko.ilievski@posta.mk</div></div>
    <div class="option">
      <svg width="12" height="12" viewBox="0 0 12 12"><circle cx="6" cy="6" r="5" fill="none" stroke="var(--green)" stroke-width="1.2"/><path d="M3.5 6l2 2 3-4" fill="none" stroke="var(--green)" stroke-width="1.2"/></svg>
      Добиј код преку СМС
    </div>
    <div class="option">
      <svg width="12" height="12" viewBox="0 0 12 12"><circle cx="6" cy="6" r="5" fill="none" stroke="var(--green)" stroke-width="1.2"/></svg>
      Добиј код преку Е-Пошта
    </div>
    <div class="spacer"></div>
    <div class="btn btn-primary">Прати код</div>
    <div class="btn btn-secondary">Промени лозинка</div>
    <div class="bottom-gap"></div>
  </section>

  <section class="screen screen-pay">
    <div class="screen-brand"><span class="brand-dot"></span><span class="brand-name">Градски Паркинг</span></div>
    <div class="field"><div class="field-label">паркинг зона</div><div class="field-value">Зона 1</div></div>
    <div class="field"><div class="field-label">времетраење</div><div class="field-value">2 Часови</div></div>
    <div class="field"><div class="field-label">регистарска таблица</div><div class="field-value">SK482TA</div></div>
    <div class="spacer"></div>
    <div class="btn btn-primary">Плати паркинг</div>
    <div style="height:12px"></div>
    <nav class="tabbar">
      <div class="tab">
        <svg width="16" height="16" viewBox="0 0 16 16"><rect x="1" y="1" width="14" height="14" rx="2" fill="none" stroke="var(--green)" stroke-width="1.3"/><path d="M6 12V4h3a2 2 0 010 4H6" fill="none" stroke="var(--green)" stroke-width="1.3"/></svg>
        Карта
      </div>
      <div class="tab">
        <svg width="16" height="18" viewBox="0 0 16 18"><path d="M8 17s6-6 6-10A6 6 0 002 7c0 4 6 10 6 10z" fill="none" stroke="var(--green)" stroke-width="1.3"/><circle cx="8" cy="7" r="2.5" fill="none" stroke="var(--green)" stroke-width="1.2"/></svg>
        МКарта
      </div>
      <div class="tab">
        <svg width="16" height="16" viewBox="0 0 16 16"><path d="M3 15V2h10l-2 3.5L13 9H3" fill="none" stroke="var(--green)" stroke-width="1.3"/></svg>
        Извештај
      </div>
    </nav>
  </section>
</main>

<div class="thanks">
  <svg class="thanks-bubble" viewBox="0 0 392 200" aria-hidden="true">
    <defs>
      <linearGradient id="bubbleFill" x1="0" y1="0" x2="1" y2="1">
        <stop offset="0" stop-color="#3dcc25"/>
        <stop offset="1" stop-color="#5ab04a"/>
      </linearGradient>
    </defs>
    <path d="M82 0H310a82 82 0 0182 82v36c0 40-20 70-62 80 10-20 4-40-30-36H82A82 82 0 010 80 82 82 0 0182 0z" fill="url(#bubbleFill)"/>
  </svg>
  <div class="thanks-text">Thank you!</div>
</div>

</body>
</html>
```